Creative, Colorful, Dynamic Infographic for Global Non-Profit

We are a global arts and education non-profit in need of an infographic that illustrates four key skills embedded in our work: Curiosity, Listening, Imagination, Postive Action.
We work primarily with educators, students, and artists who use the power of personal stories to build community and connection and to bridge divides.
Our new brand guidelines, logos, and fonts are here: https://stylekit.example/quillbridge-7
I've attached a mock-up of the graphic and the required text. (Note the attached design was created by a staff person, your final design does not need to be the same. The color scheme and text of the final design should match the brand guidelines above.)
The graphic will be used for both web and print media and should include the purple Quillbridge 7 logo (also attached).
Ideally the final design will delight audiences and spark interest in our work.

```html
<!DOCTYPE html>
<html lang="en">
<head>
<meta charset="utf-8">
<title>Quillbridge 7 – 4 Key Skills</title>
<link href="https://fonts.googleapis.com/css2?family=Montserrat:wght@500;600;700;800&family=Playfair+Display:wght@700;800&display=swap" rel="stylesheet">
<style>
  :root {
    --purple: #663399;
    --navy: #1f1b3f;
    --blue: #1f6bc4;
    --red: #e94141;
    --ink: #1a1a1a;
    --panel: #f2f2f2;
    --card: #ffffff;
    --backdrop: #e4e4e4;
    --dash: #8a8a8a;
  }
  * { box-sizing: border-box; margin: 0; padding: 0; }
  html, body { width: 700px; height: 1200px; overflow: hidden; }
  body { background: var(--backdrop); position: relative; font-family: "Montserrat", Arial, sans-serif; }

  .poster-frame { position: absolute; left: 0; top: 352px; width: 700px; height: 495px; overflow: hidden; }
  .poster {
    position: absolute; left: 0; top: 0;
    width: 1238px; height: 875px;
    background: var(--card);
    transform: scale(0.5654); transform-origin: 0 0;
  }

  /* header */
  .brand-dot { position: absolute; left: 196px; top: 48px; width: 62px; height: 62px; border-radius: 50%; background: var(--purple); }
  .brand-name { position: absolute; left: 272px; top: 62px; font-size: 26px; font-weight: 600; letter-spacing: 1px; color: var(--purple); line-height: 34px; }
  .title-number { position: absolute; left: 536px; top: 22px; font-size: 112px; font-weight: 800; color: var(--purple); line-height: 1; z-index: 2; text-shadow: 4px 0 0 var(--card); }
  .title-bar {
    position: absolute; left: 596px; top: 43px; width: 425px; height: 73px;
    background: var(--purple); border-radius: 37px;
    color: #fff; font-size: 54px; font-weight: 800; line-height: 73px; padding-left: 43px; letter-spacing: 0.5px;
  }

  /* panel */
  .panel { position: absolute; left: 36px; top: 134px; width: 1166px; height: 682px; background: var(--panel); }
  .guide { position: absolute; left: 0; top: 0; }
  .cycle { position: absolute; left: 372px; top: 224px; }

  .link-note {
    position: absolute; text-align: center; font-size: 15px; font-weight: 700; line-height: 18.5px; color: var(--ink);
    background: var(--panel); padding: 2px 6px; white-space: nowrap;
  }
  .note-top { left: 473px; top: 149px; width: 240px; }
  .note-left { left: 166px; top: 430px; width: 216px; }
  .note-right { left: 831px; top: 432px; width: 196px; }
  .note-bottom { left: 514px; top: 720px; width: 190px; }

  .skill { position: absolute; background: var(--panel); padding: 4px 6px; white-space: nowrap; }
  .skill h2 { font-family: "Playfair Display", Georgia, serif; font-weight: 800; font-size: 40px; line-height: 46px; }
  .skill p { font-size: 15px; font-weight: 500; line-height: 18.5px; color: var(--ink); margin-top: 4px; }
  .skill-left { left: 151px; }
  .skill-right { right: 151px; text-align: right; }
  .skill-top { top: 218px; }
  .skill-bottom { top: 590px; }
  .curiosity h2 { color: var(--purple); }
  .action h2 { color: var(--blue); }
  .listening h2 { color: var(--navy); }
  .imagination h2 { color: var(--red); }

  .site-url { position: absolute; left: 0; width: 1238px; top: 826px; text-align: center; font-size: 22px; font-weight: 600; letter-spacing: 2.5px; color: var(--ink); }
</style>
</head>
<body>
<div class="poster-frame">
  <main class="poster">
    <header>
      <span class="brand-dot"></span>
      <span class="brand-name">QUILLBRIDGE 7</span>
      <h1>
        <span class="title-number">4</span>
        <span class="title-bar">KEY SKILLS</span>
      </h1>
    </header>

    <section class="panel" aria-hidden="true"></section>

    <svg class="guide" width="1238" height="875" viewBox="0 0 1238 875" aria-hidden="true">
      <circle cx="612" cy="464" r="298" fill="none" stroke="var(--dash)" stroke-width="1.2" stroke-dasharray="4 3"/>
      <polygon points="690,172 708,172 701,190" fill="var(--blue)"/>
      <polygon points="305,410 323,410 313,427" fill="var(--purple)"/>
      <polygon points="505,733 505,751 522,745" fill="var(--red)"/>
      <polygon points="886,520 902,522 898,503" fill="var(--blue)"/>
    </svg>

    <svg class="cycle" width="480" height="480" viewBox="-240 -240 480 480" aria-label="Cycle of four skills">
      <g stroke="#fff" stroke-width="10" stroke-linejoin="round" paint-order="stroke">
        <path class="seg-curiosity" fill="var(--purple)" d="M96.2,-181.0 A205,205 0 0 0 -137.2,-152.3 L-153.9,-170.9 L-138.6,-80 L-60.2,-66.9 L-76.9,-85.5 A115,115 0 0 1 54.0,-101.5 Z"/>
        <path class="seg-listening" fill="var(--navy)" d="M-181.0,-96.2 A205,205 0 0 0 -152.3,137.2 L-170.9,153.9 L-80,138.6 L-66.9,60.2 L-85.5,76.9 A115,115 0 0 1 -101.5,-54.0 Z"/>
        <path class="seg-imagination" fill="var(--red)" d="M-96.2,181.0 A205,205 0 0 0 137.2,152.3 L153.9,170.9 L138.6,80 L60.2,66.9 L76.9,85.5 A115,115 0 0 1 -54.0,101.5 Z"/>
        <path class="seg-action" fill="var(--blue)" d="M181.0,96.2 A205,205 0 0 0 152.3,-137.2 L170.9,-153.9 L80,-138.6 L66.9,-60.2 L85.5,-76.9 A115,115 0 0 1 101.5,54.0 Z"/>
      </g>
      <circle r="57" fill="var(--purple)"/>

      <g fill="#fff" font-family="Playfair Display, Georgia, serif" font-weight="700" font-size="42" text-anchor="middle">
        <text x="-18" y="-140">01</text>
        <text x="-158" y="30">02</text>
        <text x="42" y="148">03</text>
        <text x="148" y="-14">04</text>
      </g>

      <g fill="#fff" stroke="#fff" stroke-linecap="round">
        <circle cx="-92" cy="-148" r="15" stroke="none"/>
        <rect x="-99" y="-132" width="14" height="10" rx="2" stroke="none"/>
        <line x1="-118" y1="-150" x2="-124" y2="-150" stroke-width="3"/>
        <line x1="-66" y1="-150" x2="-60" y2="-150" stroke-width="3"/>

        <path d="M-154,72 a16,18 0 1 1 24,14 q-6,6 -8,14 a8,8 0 0 1 -14,-2" fill="none" stroke-width="7"/>
        <line x1="-120" y1="70" x2="-106" y2="64" stroke-width="3"/>
        <line x1="-120" y1="80" x2="-104" y2="80" stroke-width="3"/>
        <line x1="-120" y1="90" x2="-106" y2="96" stroke-width="3"/>

        <circle cx="112" cy="104" r="19" stroke="none"/>
        <rect x="100" y="114" width="22" height="20" rx="3" stroke="none"/>

        <g transform="translate(2,-18)">
          <polygon points="96,-110 99,-103 106,-103 100,-98 103,-91 96,-95 89,-91 92,-98 86,-103 93,-103" stroke="none"/>
          <polygon points="116,-116 119,-109 126,-109 120,-104 123,-97 116,-101 109,-97 112,-104 106,-109 113,-109" stroke="none"/>
          <polygon points="136,-110 139,-103 146,-103 140,-98 143,-91 136,-95 129,-91 132,-98 126,-103 133,-103" stroke="none"/>
        </g>
        <g transform="translate(2,-30)">
          <rect x="94" y="-74" width="10" height="24" rx="2" stroke="none"/>
          <path d="M108,-50 v-24 l10,-16 q6,0 5,8 l-2,8 h14 q6,0 5,7 l-3,15 q-1,4 -6,4 z" stroke="none"/>
        </g>
      </g>
    </svg>

    <p class="link-note note-top">Your positive actions<br>will make you curious<br>about what else is possible.</p>
    <p class="link-note note-left">Your curiosity will allow<br>you to listen</p>
    <p class="link-note note-right">Your imagination<br>identifies positive<br>actions.</p>
    <p class="link-note note-bottom">Your listening will<br>allow you to take in<br>new information</p>

    <article class="skill skill-left skill-top curiosity">
      <h2>Curiosity</h2>
      <p>Focus on how you can learn from<br>another’s knowledge and experience<br>Your curiosity allows you to listen</p>
    </article>
    <article class="skill skill-right skill-top action">
      <h2>Positive action</h2>
      <p>Show your words and actions matter<br>Your positive actions lead to curiosity<br>about what else is possible</p>
    </article>
    <article class="skill skill-left skill-bottom listening">
      <h2>Listening</h2>
      <p>Seek to understand before<br>speaking Your listening allows you<br>to take in new information</p>
    </article>
    <article class="skill skill-right skill-bottom imagination">
      <h2>Imagination</h2>
      <p>Consider possibilities beyond what<br>you know Your imagination can spark<br>positive action</p>
    </article>

    <footer class="site-url">stylekit.example/quillbridge-7</footer>
  </main>
</div>
</body>
</html>
```